Modern business card design for professional copywriter

I'd like a business card design that I can use to have my cards printed out by plink.com as a squared corners business card (see artwork and design guidelines here: https://help.plink.com/hc/en-gb/sections/300481726-PLINK-Product-Templates)

The design should be clean and modern and reflect the colours, tone and branding on my website: https://noravestrel.com.au

Target Market(s)

Professionals, B2B small business owners

Industry/Entity Type

Business

Contact Information for Business Card

Nora Vestrel
m: 0427 593 864
e: nora@noravestrel.com.au
w: noravestrel.com.au

Font styles to use
Sans Serif

Requirements
Must have
• Tagline: "Sharp wording for ambitious business owners"
• Brand colours: fd8000, 009984, 666666 and black
Nice to have

```html
<!DOCTYPE html>
<html lang="en">
<head>
<meta charset="utf-8">
<title>Nora Vestrel – Business Card</title>
<link rel="stylesheet" href="https://fonts.googleapis.com/css2?family=Cinzel:wght@400&family=Questrial&family=Noto+Sans:wght@400&display=swap">
<style>
  :root {
    --stage: #003462;
    --brand-orange: #fd8000;
    --brand-teal: #009984;
    --brand-grey: #666666;
    --fold-shadow: #8f4a0d;
    --card-light: #ffffff;
    --ink: #111111;
    --tagline: #f2f2f2;
    --tagline-muted: #9a9a9a;
  }
  html, body {
    margin: 0;
    width: 1200px;
    height: 1200px;
    overflow: hidden;
    background: var(--stage);
  }
  .artboard { display: block; width: 1200px; height: 1200px; }
  .brand-name { font-family: "Questrial", sans-serif; fill: var(--brand-teal); }
  .brand-descriptor { font-family: "Questrial", sans-serif; fill: var(--brand-grey); letter-spacing: 9px; }
  .tagline { font-family: "Cinzel", serif; fill: var(--tagline); }
  .tagline--small { fill: var(--tagline-muted); }
  .holder-name { font-family: "Cinzel", serif; fill: var(--ink); }
  .holder-role, .contact-line { font-family: "Noto Sans", sans-serif; fill: var(--ink); }
  .bracket { fill: none; stroke: var(--brand-orange); stroke-width: 3; }
  .envelope-fold { fill: none; stroke: var(--brand-teal); stroke-width: 3.5; stroke-linejoin: round; }
  .mouse-wheel { fill: none; stroke: var(--brand-grey); stroke-width: 3; }
</style>
</head>
<body>
<svg class="artboard" viewBox="0 0 1200 1200" xmlns="http://www.w3.org/2000/svg">
  <defs>
    <radialGradient id="card-glow" cx="0.55" cy="0.6" r="0.75">
      <stop offset="0" stop-color="#242424"/>
      <stop offset="1" stop-color="#050505"/>
    </radialGradient>
  </defs>

  <!-- Front face -->
  <g class="card card--front">
    <rect x="145.6" y="30.4" width="916.8" height="550.4" fill="url(#card-glow)"/>
    <rect x="145.6" y="565.6" width="916.8" height="15.2" fill="var(--brand-orange)"/>
    <path class="bracket" d="M376 209.6 H265.6 V328 H286"/>
    <path class="bracket" d="M844 209.6 H940.8 V328 H920"/>
    <rect x="384" y="206" width="18" height="18" fill="var(--brand-orange)"/>
    <text class="brand-name" x="412" y="246" font-size="62" textLength="416" lengthAdjust="spacingAndGlyphs">Nora Vestrel</text>
    <text class="brand-descriptor" x="614" y="270" font-size="19">COPYWRITER</text>
    <text class="tagline" x="293.6" y="337" font-size="27" textLength="618" lengthAdjust="spacingAndGlyphs">Sharp wording for ambitious business owners</text>
  </g>

  <!-- Back face -->
  <g class="card card--back">
    <rect x="144.8" y="607.2" width="560" height="550.4" fill="url(#card-glow)"/>
    <rect x="704.8" y="607.2" width="357.6" height="550.4" fill="var(--card-light)"/>
    <rect x="704.8" y="1142.4" width="357.6" height="15.2" fill="var(--brand-orange)"/>

    <rect x="214" y="806" width="14" height="14" fill="var(--brand-orange)"/>
    <text class="brand-name" x="236" y="858" font-size="48" textLength="318" lengthAdjust="spacingAndGlyphs">Nora Vestrel</text>
    <text class="brand-descriptor" x="388" y="874" font-size="15" style="letter-spacing:7px">COPYWRITER</text>
    <text class="tagline tagline--small" x="239" y="896" font-size="13" textLength="313" lengthAdjust="spacingAndGlyphs">Sharp wording for ambitious business owners</text>

    <text class="holder-name" x="750.4" y="689.6" font-size="44" textLength="272" lengthAdjust="spacingAndGlyphs">Nora Vestrel</text>
    <text class="holder-role" x="750.4" y="714.4" font-size="19">COPPYWRITER</text>

    <polygon points="644,729.6 704.8,707.2 704.8,729.6" fill="var(--fold-shadow)"/>
    <rect x="644" y="729.6" width="115.2" height="112" fill="var(--brand-orange)"/>
    <rect x="644" y="841.6" width="115.2" height="112" fill="var(--brand-teal)"/>
    <rect x="644" y="953.6" width="115.2" height="112.8" fill="var(--brand-grey)"/>

    <!-- phone icon -->
    <path d="M679 760 l10 -4 l12 22 l-8 6 q6 14 20 22 l7 -7 l14 12 l-6 8 q-18 2 -36 -18 q-16 -20 -13 -41 z" fill="var(--card-light)"/>
    <!-- envelope icon -->
    <path d="M668 892 L701.6 866 L735 892 V922 H668 Z" fill="var(--card-light)"/>
    <path class="envelope-fold" d="M668 892 L701.6 914 L735 892"/>
    <path class="envelope-fold" d="M669 921 L693 906 M734 921 L710 906"/>
    <!-- mouse icon -->
    <rect x="676" y="982" width="50" height="62" rx="24" fill="var(--card-light)"/>
    <rect class="mouse-wheel" x="693" y="992" width="15" height="19" rx="7.5"/>

    <text class="contact-line" x="770.4" y="797.6" font-size="19.5">NUMBER: 0427.593.864</text>
    <text class="contact-line" x="770.4" y="905.6" font-size="19.5" textLength="286" lengthAdjust="spacingAndGlyphs">MAIL: nora@noravestrel.com.au</text>
    <text class="contact-line" x="770.4" y="1020.8" font-size="19.5">WEBSITE: noravestrel.com.au</text>
  </g>
</svg>
</body>
</html>
```